Cardiology practice business card

We need a business card for our cardiology practice "Bellmoor Cardiology". We have a new logo, attached below. We like the colours in the logo - red and charcoal. The front of the business card will need to have the doctors name, address, phone number and email. The back will need to have space to write 2 appointment dates and times.

```html
<!DOCTYPE html>
<html lang="en">
<head>
<meta charset="utf-8">
<title>Bellmoor Cardiology – Business Card</title>
<link rel="stylesheet" href="https://fonts.googleapis.com/css2?family=Lato:wght@400;700;900&display=swap">
<style>
  :root {
    --stage: #a4a4a4;
    --paper-light: #f4f4f3;
    --paper-mid: #d9d9d8;
    --charcoal: #2d2e32;
    --red: #e0262b;
    --red-deep: #b81d22;
    --ink: #3a3b3f;
    --white: #ffffff;
    --silver-light: #f6f6f6;
    --silver-dark: #bdbdbd;
  }
  * { margin: 0; padding: 0; box-sizing: border-box; }
  html, body { width: 1200px; height: 1000px; overflow: hidden; }
  body {
    position: relative;
    background: var(--stage);
    font-family: "Lato", sans-serif;
  }
  .card {
    position: absolute;
    left: 196px;
    width: 833px;
    border-radius: 16px;
    overflow: hidden;
    box-shadow: 0 3px 6px rgba(0,0,0,0.25);
  }
  .card--front {
    top: 13px;
    height: 477px;
    background: radial-gradient(ellipse at 50% 40%, var(--paper-light) 0%, #e8e8e7 55%, var(--paper-mid) 100%);
  }
  .card--back {
    top: 509px;
    height: 476px;
    background: var(--charcoal);
  }
  .brand {
    position: absolute;
    font-weight: 900;
    text-transform: uppercase;
    line-height: 1.05;
    letter-spacing: 0.04em;
  }
  .card--front .brand {
    left: 0; right: 0; top: 170px;
    text-align: center;
    font-size: 56px;
    color: var(--red);
  }
  .card--back .brand {
    left: 70px; top: 166px;
    font-size: 30px;
    color: var(--white);
  }
  .doctor {
    position: absolute;
    left: 414px; top: 74px;
    font-size: 31px;
    font-weight: 700;
    color: var(--white);
  }
  .doctor .title-prefix { color: var(--red); }
  .role {
    position: absolute;
    left: 415px; top: 116px;
    font-size: 20px;
    color: #e6e6e6;
  }
  .contacts {
    position: absolute;
    left: 414px; top: 166px;
    list-style: none;
  }
  .contacts li {
    display: flex;
    align-items: flex-start;
    font-size: 22px;
    line-height: 26px;
    color: #efefef;
    margin-bottom: 11px;
  }
  .contacts svg { flex: none; width: 24px; height: 24px; margin: 1px 15px 0 0; }
  .hours {
    position: absolute;
    top: 367px;
    width: 410px;
    height: 62px;
  }
  .hours svg { position: absolute; inset: 0; }
  .hours p {
    position: relative;
    text-align: center;
    font-size: 18px;
    line-height: 23px;
    padding-top: 7px;
  }
  .hours b { font-weight: 700; }
  .hours--primary { left: 23px; color: var(--white); }
  .hours--secondary { left: 403px; color: var(--ink); }
  .hours--secondary .label, .hours--secondary .joiner { color: var(--red-deep); font-weight: 700; }
</style>
</head>
<body>

<section class="card card--front" aria-label="Card front">
  <div class="brand">Bellmoor<br>Cardiology</div>
</section>

<section class="card card--back" aria-label="Card back">
  <div class="brand">Bellmoor<br>Cardiology</div>

  <h1 class="doctor"><span class="title-prefix">DR.</span> ADRIAN HALE</h1>
  <p class="role">General Surgeon</p>

  <ul class="contacts">
    <li>
      <svg viewBox="0 0 24 24" aria-hidden="true"><rect x="1" y="1" width="22" height="22" rx="4" fill="none" stroke="#e0262b" stroke-width="2"/><path d="M8 6.5c-1 .6-1.6 1.6-1.2 3 .8 3 3.6 6.1 6.8 7.4 1.4.5 2.4 0 3-.9l-2-2-1.4.7c-1.4-.7-2.7-2-3.4-3.4l.7-1.4z" fill="#e0262b"/></svg>
      044-555 210 347
    </li>
    <li>
      <svg viewBox="0 0 24 24" aria-hidden="true"><rect x="1" y="1" width="22" height="22" rx="4" fill="none" stroke="#e0262b" stroke-width="2"/><path d="M5.5 12.5 18 6.5l-3 11-3.4-3.2-2 2v-3.3z" fill="#e0262b"/></svg>
      info@bellmoor.com
    </li>
    <li>
      <svg viewBox="0 0 24 24" aria-hidden="true"><rect x="1" y="1" width="22" height="22" rx="4" fill="none" stroke="#e0262b" stroke-width="2"/><path d="M12 4.8a4.8 4.8 0 0 0-4.8 4.8c0 3.6 4.8 9 4.8 9s4.8-5.4 4.8-9A4.8 4.8 0 0 0 12 4.8zm0 6.6a1.8 1.8 0 1 1 0-3.6 1.8 1.8 0 0 1 0 3.6z" fill="#e0262b"/></svg>
      <span>412 N Linden St Harlow,<br>FL 33520, 27150 W Marrow<br>Bay Road Calder, FL 33914</span>
    </li>
  </ul>

  <div class="hours hours--primary">
    <svg viewBox="0 0 410 62" preserveAspectRatio="none" aria-hidden="true"><path d="M28 0H405L380 52Q376 60 366 60H0Z" fill="#e0262b"/></svg>
    <p><b>MONDAY:</b> <b>6:00</b> PM TO <b>8:00</b> PM<br><b>FRIDAY:</b> <b>4:00</b> PM TO <b>6:00</b> PM</p>
  </div>
  <div class="hours hours--secondary">
    <svg viewBox="0 0 410 62" preserveAspectRatio="none" aria-hidden="true"><defs><linearGradient id="silver" x1="0" y1="0" x2="0" y2="1"><stop offset="0" stop-color="#f6f6f6"/><stop offset="1" stop-color="#bdbdbd"/></linearGradient></defs><path d="M28 0H402L382 52Q378 60 368 60H0Z" fill="url(#silver)"/></svg>
    <p><span class="label">TUESDAY:</span> <b>6:00</b> PM <span class="joiner">TO</span> <b>8:00</b> PM<br><span class="label">WEDNESDAY:</span> <b>4:00</b> PM <span class="joiner">TO</span> <b>6:00</b> PM</p>
  </div>
</section>

</body>
</html>
```